Business Card Design - Photographer

I am a landscape photographer and I require a business card design. 

I require two designs:
1)  a double sided business card
 and
b)  a single sided business card 

The single sided design can either be the same as the double sided (with just one side having all the information)....or it can be an entire new design. Its up to you.

My corporate colours are (CMYK):

Blue   69, 32, 0, 0
Grey  72,  64,  47,  31
Green  32,  2,  91,  0
Yellow   0, 19, 92, 0
Orange  0, 39, 75, 0

Colour space in final file should be in CMYK.

The details that need to be included on the card:

- Use the provided Logo
- Name: Lukas Wendrovski
- Email:   sales@vistaplume.com.au
- Website:    vistaplume.com.au
- Chatterly:    twitter.com/vistaplume
- Friendloop:   facebook.com/vistaplume
- Mobile  0415 309 662

Please use the attached template to design the logo to the specified size, including the marked bleed lines. I have also attached my logo in PNG (transparent background) and ai format for you to use.

The final file should be:
- Photoshop version with layers so I can edit the name/text etc. All non vector files should be high resolution at 1039 x 697 pixels at 300 dpi.

I also require a file as:
- Vector based PDF

Anyway questions please contact me.

Thank you

Industry/Entity Type

Landscape

Logo styles of interest
Pictorial/Combination Logo
Abstract Logo
Wordmark Logo
Lettermark Logo
Requirements
Must have
• The details that need to be included on the card:

- Use the provided Logo
- Name: Lukas Wendrovski
- Email: sales@vistaplume.com.au
- Website: vistaplume.com.au
- Chatterly: twitter.com/vistaplume
- Friendloop: facebook.com/vistaplume
- Mobile 0415 309 662

```html
<!DOCTYPE html>
<html lang="en">
<head>
<meta charset="utf-8">
<title>Vista Plume – Business Card</title>
<link rel="stylesheet" href="https://fonts.googleapis.com/css2?family=Arimo:wght@400&display=swap">
<style>
  :root {
    --page-bg: #8a8a8a;
    --card-bg: #1b1b1b;
    --card-bg-alt: #232323;
    --hole: #ffffff;
    --text: #ffffff;
    --brand-grey: #8c9098;
    --lens-amber: #d9782a;
    --lens-deep: #5a2410;
    --social-blue: #2a9fd6;
    --social-navy: #2f4f9a;
  }
  html, body {
    margin: 0;
    padding: 0;
    width: 1200px;
    height: 1200px;
    overflow: hidden;
    background: var(--page-bg);
  }
  .card {
    position: absolute;
    left: 40px;
    top: 224px;
    width: 1120px;
    height: 752px;
    overflow: hidden;
    background:
      repeating-linear-gradient(45deg, rgba(255,255,255,0.015) 0 2px, transparent 2px 4px),
      linear-gradient(90deg, var(--card-bg-alt), var(--card-bg));
    font-family: "Arimo", Arial, sans-serif;
    color: var(--text);
  }
  .lens-photo {
    position: absolute;
    left: 500px;
    top: 0;
    width: 620px;
    height: 752px;
    background:
      radial-gradient(ellipse 150px 230px at 330px 375px, var(--lens-amber) 0%, var(--lens-deep) 60%, #140d0a 100%),
      #0c0c0c;
    background-repeat: no-repeat;
    background-size: 100% 100%;
    -webkit-mask: radial-gradient(circle 440px at 330px 375px, #000 60%, transparent 100%);
            mask: radial-gradient(circle 440px at 330px 375px, #000 60%, transparent 100%);
  }
  .sprocket {
    position: absolute;
    width: 68px;
    height: 68px;
    background: var(--hole);
  }
  .brand-mark {
    position: absolute;
    left: 213px;
    top: 125px;
    width: 140px;
    height: 140px;
    border-radius: 50%;
    background: #3a3d44;
  }
  .brand-name {
    position: absolute;
    left: 0;
    width: 566px;
    top: 278px;
    text-align: center;
    font-size: 38px;
    letter-spacing: 2px;
    color: var(--brand-grey);
  }
  .person-name {
    position: absolute;
    left: 83px;
    top: 376px;
    margin: 0;
    font-size: 32px;
    font-weight: 400;
  }
  .contact-list {
    list-style: none;
    margin: 0;
    padding: 0;
  }
  .contact-item {
    position: absolute;
    left: 55px;
    display: flex;
    align-items: center;
    font-size: 20px;
    height: 38px;
    white-space: nowrap;
  }
  .contact-item .icon {
    width: 34px;
    height: 34px;
    margin-right: 20px;
    flex: none;
  }
  .social-square-one { background: var(--social-blue); }
  .social-square-two { background: var(--social-navy); }
</style>
</head>
<body>
  <div class="card">
    <div class="lens-photo" role="img" aria-label="Close-up photograph of a camera lens with amber and orange reflections in the glass"></div>

    <div class="sprocket" style="left:57px;top:42px"></div>
    <div class="sprocket" style="left:192px;top:42px"></div>
    <div class="sprocket" style="left:326px;top:42px"></div>
    <div class="sprocket" style="left:461px;top:42px"></div>
    <div class="sprocket" style="left:593px;top:42px"></div>
    <div class="sprocket" style="left:730px;top:42px"></div>
    <div class="sprocket" style="left:862px;top:42px"></div>
    <div class="sprocket" style="left:998px;top:42px"></div>

    <div class="sprocket" style="left:57px;top:643px"></div>
    <div class="sprocket" style="left:192px;top:643px"></div>
    <div class="sprocket" style="left:326px;top:643px"></div>
    <div class="sprocket" style="left:461px;top:643px"></div>
    <div class="sprocket" style="left:593px;top:643px"></div>
    <div class="sprocket" style="left:730px;top:643px"></div>
    <div class="sprocket" style="left:862px;top:643px"></div>
    <div class="sprocket" style="left:998px;top:643px"></div>

    <div class="brand-mark"></div>
    <div class="brand-name">VISTA PLUME</div>

    <h1 class="person-name">Lukas Wendrovski</h1>

    <ul class="contact-list">
      <li class="contact-item" style="top:431px">
        <svg class="icon" viewBox="0 0 34 34" fill="none" stroke="#fff" stroke-width="2">
          <rect x="2" y="8" width="30" height="19"/>
          <path d="M2 8 L17 19 L32 8 M2 27 L13 16 M32 27 L21 16"/>
        </svg>
        sales@vistaplume.com.au
      </li>
      <li class="contact-item" style="top:469px">
        <svg class="icon" viewBox="0 0 34 34" fill="none" stroke="#fff" stroke-width="2">
          <circle cx="17" cy="17" r="14"/>
          <ellipse cx="17" cy="17" rx="6" ry="14"/>
          <path d="M3 17 H31 M6 9 H28 M6 25 H28"/>
        </svg>
        www.vistaplume.com.au
      </li>
      <li class="contact-item" style="top:506px">
        <svg class="icon" viewBox="0 0 34 34" fill="none" stroke="#fff" stroke-width="2" stroke-linejoin="round">
          <path d="M8 3 L13 9 L10 13 Q13 20 20 24 L24 21 L31 26 L27 31 Q15 31 7 20 Q3 12 8 3 Z"/>
        </svg>
        0415 309 662
      </li>
      <li class="contact-item" style="top:552px">
        <span class="icon social-square-one"></span>
        Chatterly.com/vistaplume
      </li>
      <li class="contact-item" style="top:595px">
        <span class="icon social-square-two"></span>
        Friendloop.com/vistaplume
      </li>
    </ul>
  </div>
</body>
</html>
```